Business Card Design Project

Looking to have a new business card created.

The card needs to be sort of two cards attached in the centre creating a flip card so we can write in the centre.

First side with my information at the director / licensee and then the back side with my assistant's details.

Inside with minimal information, facebook link/sign and then lines to write on.

www.norlandestates.com.au is my website to show colours and designs that I like.

Target Market(s)

Property Owners, Property Investors, Tenants, rental clients, Tradesman.

Industry/Entity Type

Business

Requirements
Must have
• Professional & symmetrical.

Am getting pro photos for myself & assistance, so a space for these once received.

```html
<!DOCTYPE html>
<html lang="en">
<head>
<meta charset="utf-8">
<title>Norland Estates – Flip Business Card</title>
<link rel="stylesheet" href="https://fonts.googleapis.com/css2?family=Open+Sans:wght@400;600;700&family=Quicksand:wght@400;500&display=swap">
<style>
  :root {
    --stage-top: #e6e6e6;
    --stage-bottom: #c9c9c9;
    --paper: #ffffff;
    --teal-deep: #0c2530;
    --teal-mid: #1a4454;
    --teal-glow: #24596a;
    --ink: #333a3f;
    --ink-soft: #6f7f87;
    --brand: #5f7f93;
    --link: #3c4c8c;
    --label: #7d8c96;
  }
  * { box-sizing: border-box; margin: 0; padding: 0; }
  html, body { width: 833px; height: 1200px; overflow: hidden; background: var(--paper); }
  .sheet { position: relative; width: 833px; height: 1200px; }

  /* outer faces */
  .outer-faces {
    position: absolute; left: 0; top: 0; width: 833px; height: 600px;
    background: linear-gradient(180deg, var(--stage-top), var(--stage-bottom));
  }
  .side-label {
    position: absolute; font-family: "Quicksand", sans-serif; font-weight: 400;
    color: var(--label); font-size: 20px; letter-spacing: 1px;
  }
  .side-label.front { left: 206px; top: 80px; }
  .side-label.back { left: 540px; top: 448px; }

  .card {
    position: absolute; width: 380px; height: 232px; background: var(--paper);
    box-shadow: 0 6px 14px rgba(0,0,0,0.22); overflow: hidden;
  }
  .card.front-card { left: 410px; top: 62px; }
  .card.back-card { left: 44px; top: 200px; }
  .card-bg { position: absolute; inset: 0; }
  .card-brand {
    position: absolute; left: 26px; top: 26px;
    font-family: "Open Sans", sans-serif; font-weight: 600; font-size: 19px;
    color: var(--brand); letter-spacing: 0.5px;
  }
  .card-name {
    position: absolute; left: 22px; top: 96px; color: var(--paper);
    font-family: "Open Sans", sans-serif; font-weight: 400; font-size: 25px; line-height: 1;
  }
  .card-role {
    position: absolute; left: 23px; top: 126px; color: var(--paper);
    font-family: "Open Sans", sans-serif; font-weight: 700; font-size: 7.5px; letter-spacing: 0.4px;
  }
  .card-contacts {
    position: absolute; left: 180px; top: 160px; list-style: none; color: var(--paper);
    font-family: "Open Sans", sans-serif; font-size: 8.5px; line-height: 13.5px;
  }
  .card-contacts li { display: flex; align-items: center; gap: 6px; }
  .card-contacts svg { width: 8px; height: 8px; flex: none; }

  /* inside */
  .inside-label {
    position: absolute; left: 84px; top: 852px;
    font-family: "Quicksand", sans-serif; font-weight: 400; font-size: 38px;
    color: var(--label); letter-spacing: 1px;
  }
  .inside-face { position: absolute; left: 289px; top: 600px; width: 544px; height: 600px; background: var(--paper); }
  .inside-edges { position: absolute; inset: 0; }
  .inside-brand {
    position: absolute; left: 56px; top: 36px;
    font-family: "Open Sans", sans-serif; font-weight: 600; font-size: 30px;
    color: var(--brand); letter-spacing: 0.5px;
  }
  .inside-details {
    position: absolute; left: 0; right: 0; top: 196px; text-align: center;
    font-family: "Open Sans", sans-serif; font-size: 18px; line-height: 23px; color: var(--ink);
  }
  .inside-details p + p { margin-top: 23px; }
  .inside-details a { color: var(--link); text-decoration: none; }
  .inside-web {
    position: absolute; left: 70px; top: 1150px; display: flex; align-items: center; gap: 12px;
    font-family: "Open Sans", sans-serif; font-size: 19px; color: var(--ink-soft);
  }
  .inside-web { top: auto; bottom: 18px; }
  .inside-web svg { width: 18px; height: 18px; }
</style>
</head>
<body>
<main class="sheet">

  <section class="outer-faces" aria-label="Outer faces of the flip card">
    <span class="side-label front">front</span>
    <span class="side-label back">back</span>

    <article class="card front-card">
      <svg class="card-bg" viewBox="0 0 380 232" preserveAspectRatio="none" aria-hidden="true">
        <defs>
          <radialGradient id="tealFront" cx="0.45" cy="0.55" r="0.8">
            <stop offset="0" stop-color="#24596a"/>
            <stop offset="0.6" stop-color="#1a4454"/>
            <stop offset="1" stop-color="#0c2530"/>
          </radialGradient>
        </defs>
        <path d="M0 86 Q190 74 380 104 L380 232 L0 232 Z" fill="url(#tealFront)"/>
        <path d="M150 86 Q260 84 352 106 Q262 92 150 86 Z" fill="#ffffff"/>
      </svg>
      <div class="card-brand">Norland Estates</div>
      <h2 class="card-name">Clara Whitfield</h2>
      <p class="card-role">MANAGING DIRECTOR / PRINCIPAL REA</p>
      <ul class="card-contacts">
        <li><svg viewBox="0 0 10 10"><path d="M3 1 L4.5 3 L3.5 4.2 Q4.5 6 6 6.6 L7 5.5 L9 7 L8 9 Q3 9 1 2.5 Z" fill="#fff"/></svg>1300 555 210</li>
        <li><svg viewBox="0 0 10 10"><path d="M3 1 L4.5 3 L3.5 4.2 Q4.5 6 6 6.6 L7 5.5 L9 7 L8 9 Q3 9 1 2.5 Z" fill="#fff"/></svg>0400 555 318</li>
        <li><svg viewBox="0 0 10 10"><rect x="0.5" y="2" width="9" height="6" fill="none" stroke="#fff"/><path d="M0.5 2 L5 5.5 L9.5 2" fill="none" stroke="#fff"/></svg>clara@norlandestates.com.au</li>
        <li><svg viewBox="0 0 10 10"><circle cx="5" cy="5" r="4.3" fill="none" stroke="#fff"/><ellipse cx="5" cy="5" rx="1.8" ry="4.3" fill="none" stroke="#fff" stroke-width="0.7"/><path d="M0.7 5 H9.3" stroke="#fff" stroke-width="0.7"/></svg>www.norlandestates.com.au</li>
      </ul>
    </article>

    <article class="card back-card">
      <svg class="card-bg" viewBox="0 0 380 232" preserveAspectRatio="none" aria-hidden="true">
        <defs>
          <radialGradient id="tealBack" cx="0.45" cy="0.55" r="0.8">
            <stop offset="0" stop-color="#24596a"/>
            <stop offset="0.6" stop-color="#1a4454"/>
            <stop offset="1" stop-color="#0c2530"/>
          </radialGradient>
        </defs>
        <path d="M0 86 Q190 74 380 104 L380 232 L0 232 Z" fill="url(#tealBack)"/>
        <path d="M150 86 Q260 84 352 106 Q262 92 150 86 Z" fill="#ffffff"/>
      </svg>
      <div class="card-brand">Norland Estates</div>
      <h2 class="card-name">Nadia Brooks</h2>
      <p class="card-role">RENTAL MANAGER</p>
      <ul class="card-contacts">
        <li><svg viewBox="0 0 10 10"><path d="M3 1 L4.5 3 L3.5 4.2 Q4.5 6 6 6.6 L7 5.5 L9 7 L8 9 Q3 9 1 2.5 Z" fill="#fff"/></svg>1300 555 210</li>
        <li><svg viewBox="0 0 10 10"><path d="M3 1 L4.5 3 L3.5 4.2 Q4.5 6 6 6.6 L7 5.5 L9 7 L8 9 Q3 9 1 2.5 Z" fill="#fff"/></svg>0400 555 742</li>
        <li><svg viewBox="0 0 10 10"><rect x="0.5" y="2" width="9" height="6" fill="none" stroke="#fff"/><path d="M0.5 2 L5 5.5 L9.5 2" fill="none" stroke="#fff"/></svg>nadia@norlandestates.com.au</li>
        <li><svg viewBox="0 0 10 10"><circle cx="5" cy="5" r="4.3" fill="none" stroke="#fff"/><ellipse cx="5" cy="5" rx="1.8" ry="4.3" fill="none" stroke="#fff" stroke-width="0.7"/><path d="M0.7 5 H9.3" stroke="#fff" stroke-width="0.7"/></svg>www.norlandestates.com.au</li>
      </ul>
    </article>
  </section>

  <span class="inside-label">inside</span>

  <section class="inside-face" aria-label="Inside of the flip card">
    <svg class="inside-edges" viewBox="0 0 544 600" preserveAspectRatio="none" aria-hidden="true">
      <defs>
        <linearGradient id="edgeTeal" x1="0" y1="0" x2="0" y2="1">
          <stop offset="0" stop-color="#0c2530"/>
          <stop offset="0.5" stop-color="#1a4454"/>
          <stop offset="1" stop-color="#0c2530"/>
        </linearGradient>
      </defs>
      <path d="M0 0 H40 Q8 300 40 600 H0 Z" fill="url(#edgeTeal)"/>
      <path d="M544 0 H502 Q534 300 502 600 H544 Z" fill="url(#edgeTeal)"/>
    </svg>
    <div class="inside-brand">Norland Estates</div>
    <div class="inside-details">
      <p>Apply online: <a href="#">http://bit.ly/nrlndes</a></p>
      <p>1300 NORLAND<br>ACN: 482 615 907</p>
      <p>Postal Address: Po Box 418, Seaview Q 4521<br>Office Location: Level 2/48 Harbour Parade,<br>&nbsp;&nbsp;&nbsp;&nbsp;&nbsp;&nbsp;&nbsp;&nbsp;&nbsp;&nbsp;Seaview Q 4521</p>
    </div>
    <div class="inside-web">
      <svg viewBox="0 0 20 20" aria-hidden="true"><circle cx="10" cy="10" r="8.5" fill="none" stroke="#6f7f87" stroke-width="1.5"/><ellipse cx="10" cy="10" rx="3.6" ry="8.5" fill="none" stroke="#6f7f87" stroke-width="1.2"/><path d="M1.5 10 H18.5" stroke="#6f7f87" stroke-width="1.2"/></svg>
      <span>www.norlandestates.com.au</span>
    </div>
  </section>

</main>
</body>
</html>
```